Price Package PDF - 2 page PDF of stylized price packages for property management firm

Looking for a 2 x A4 page PDF for our two price packages.
I would like this to be in similar style to our website www.harbourlanerentals.com.au
I have attached an example. But would like mine to be a little more stylish and modern, preferably using design similar to our website.
Words and images also attached

Target Market(s)

investment property owners, male and female, aged 30-60

Industry/Entity Type

Real Estate

Font styles to use
Sans Serif

Requirements
Must have
• split two packages onto seperate A4 pages (See example file attached)
• Contact info:
• Website: www.harbourlanerentals.com.au
• email: info@harbourlanerentals.com.au
• Phone: Tom Willard 0438 216 907, Marika Dunstan 0419 572 046
• Office Address: Suite 7, 12-14 Carrow Parade, Dee Why NSW 2099
Nice to have
• I would like to use any of the pictures provided or images of modern residential property interior or of Sydney's Northern Beaches.

```html
<!DOCTYPE html>
<html lang="en">
<head>
<meta charset="utf-8">
<title>Harbour Lane Rentals – Price Packages</title>
<link href="https://fonts.googleapis.com/css2?family=Bebas+Neue&family=Montserrat:wght@300&family=Nunito+Sans:wght@400;700;800&display=swap" rel="stylesheet">
<style>
  :root{
    --brand-blue:#1c65a3;
    --heading-blue:#1f5d99;
    --text-dark:#1d1d1f;
    --panel-grey:#f1f1f2;
    --accent-teal:#2a9a9a;
    --white:#ffffff;
  }
  *{box-sizing:border-box;margin:0;padding:0}
  html,body{width:1200px;height:1000px;overflow:hidden;background:var(--white)}
  body{position:relative;font-family:"Nunito Sans",Arial,sans-serif;color:var(--text-dark)}

  .page{position:absolute;top:115px;width:545px;height:770px;background:var(--white);
    box-shadow:0 2px 8px rgba(0,0,0,.22);overflow:hidden}
  .page--inclusive{left:44px}
  .page--management{left:613px}

  .brand{position:absolute;left:26px;top:48px;display:flex;align-items:center;gap:8px}
  .brand__mark{width:14px;height:14px;background:var(--accent-teal)}
  .brand__name{font-weight:800;font-size:21px;letter-spacing:-.2px;color:var(--text-dark)}

  .hero{position:absolute;left:0;top:107px;width:545px;height:238px;
    display:flex;align-items:center;justify-content:center}
  .page--inclusive .hero{background:linear-gradient(180deg,#5f87ab 0%,#3f6f98 45%,#2f6896 70%,#4a7ca4 100%)}
  .page--management .hero{background:linear-gradient(160deg,#56728e 0%,#3d6485 40%,#2f5d7e 70%,#5a87a4 100%)}
  .hero__title{font-family:"Montserrat",Arial,sans-serif;font-weight:300;color:var(--white);
    font-size:37px;line-height:39px;letter-spacing:1px;text-align:center;text-transform:uppercase}

  .includes{position:absolute;left:30px;top:358px;width:240px}
  .section-heading{font-family:"Bebas Neue",Impact,sans-serif;font-weight:400;font-size:20px;letter-spacing:.2px;line-height:1}
  .includes .section-heading{color:var(--text-dark);display:flex;align-items:center;gap:8px}
  .chevron{width:7px;height:12px}
  .feature-list{list-style:none;margin-top:7px}
  .feature-list li,.fee-list li{position:relative;padding-left:12px;font-size:11.6px;line-height:15.2px}
  .feature-list li::before,.fee-list li::before{content:"";position:absolute;left:0;top:4px;width:6px;height:6px;background:var(--brand-blue)}

  .fees{position:absolute;left:281px;top:345px;width:264px;height:208px;background:var(--panel-grey);padding:14px 26px 0 22px;overflow:hidden}
  .fees .section-heading{color:var(--heading-blue)}
  .fee-list{list-style:none;margin-top:6px}
  .fee-list li{line-height:17px}
  .page--management .fee-list li{line-height:15.4px}
  .fee-list li.fee-list__rate{color:var(--heading-blue)}
  .fee-list__big{font-size:13px}

  .side-photo{position:absolute;left:281px;top:553px;width:264px;height:147px}
  .page--inclusive .side-photo{background:linear-gradient(200deg,#1b7fd0 0%,#2a6aa8 45%,#16314d 100%)}
  .page--management .side-photo{background:linear-gradient(180deg,#dfe8f1 0%,#6e9cc2 40%,#3a4a5a 75%,#232a31 100%)}

  .contact-bar{position:absolute;left:0;bottom:0;width:545px;height:60px;background:var(--brand-blue);
    color:var(--white);display:flex;align-items:center;font-size:8.4px;line-height:11px;padding-left:10px;white-space:nowrap}
  .contact-bar__group{display:flex;align-items:flex-start;gap:4px;padding-right:8px}
  .contact-bar__divider{width:1px;height:36px;background:rgba(255,255,255,.7);margin-right:9px}
  .contact-bar__people{width:150px;text-align:right;padding-right:10px}
  .contact-bar__people span{opacity:.85}
  .contact-bar__address{width:142px}
  .contact-bar__web{width:158px}
  .contact-bar__line{display:flex;gap:4px}
  .contact-bar__social{display:flex;gap:6px}
  .social-square{width:11px;height:11px;background:var(--white);border-radius:2px;opacity:.9}
  .icon{width:9px;height:9px;flex:none;margin-top:1px}
</style>
</head>
<body>

<article class="page page--inclusive">
  <div class="brand"><span class="brand__mark"></span><span class="brand__name">HARBOUR LANE RENTALS</span></div>
  <div class="hero" role="img" aria-label="Blue-toned photo of a Northern Beaches harbour foreshore with apartments and pine trees">
    <h1 class="hero__title">All Inclusive<br>Package</h1>
  </div>

  <section class="includes">
    <h2 class="section-heading"><svg class="chevron" viewBox="0 0 7 12"><path d="M1 1l5 5-5 5" fill="none" stroke="#1c65a3" stroke-width="2"/></svg>Includes:</h2>
    <ul class="feature-list">
      <li>Securing Tenant</li>
      <li>Reference/Database Checking</li>
      <li>Lease Preparation and Signing</li>
      <li>Direct Debit rent collection</li>
      <li>Zero arrears policy management</li>
      <li>Payment of Rates and levies</li>
      <li>Insurance management</li>
      <li>Coordination or all repairs and maintenance</li>
      <li>Regular rent reviews and renewals</li>
      <li>Detailed ingoing, ongoing and outgoing inspections with photos and videos viewable through your personal Landlord portal</li>
      <li>Bond management &nbsp;lodging and refunding</li>
      <li>Electronic monthly and EOFY statements</li>
      <li>Annual scheduled maintenance report</li>
      <li>Regulation/compliance management</li>
      <li>Tribunal Representation</li>
    </ul>
  </section>

  <section class="fees">
    <h2 class="section-heading">All Inclusive Package:</h2>
    <ul class="fee-list">
      <li class="fee-list__rate">Management Rate: <span class="fee-list__big">10% + GST</span> of rental income</li>
      <li>Letting Fee: No Charge</li>
      <li>Advertising: No Charge</li>
      <li>Professional Photography: $199 (inc GST) 4 x Photos</li>
      <li>Statements: No Charge</li>
      <li>Lease Preparation: No Charge</li>
      <li>Renewal Fees: No Charge</li>
    </ul>
  </section>
  <div class="side-photo" role="img" aria-label="Photo of a waterfront wharf building sign against a bright blue sky"></div>

  <footer class="contact-bar">
    <div class="contact-bar__people">Tom Willard <span>✆ 0438 216 907</span><br>Marika Dunstan <span>✆ 0419 572 046</span></div>
    <div class="contact-bar__divider"></div>
    <div class="contact-bar__group contact-bar__address">
      <svg class="icon" viewBox="0 0 10 10"><path d="M5 1L1 5h1.3v4h2.2V6.5h1V9h2.2V5H9z" fill="#fff"/></svg>
      <div>Suite 7, 12-14 Carrow Parade,<br>Dee Why NSW 2099</div>
    </div>
    <div class="contact-bar__divider"></div>
    <div class="contact-bar__group contact-bar__web">
      <div>
        <div class="contact-bar__line"><svg class="icon" viewBox="0 0 10 10"><rect x="1" y="2" width="8" height="6" fill="none" stroke="#fff"/><path d="M1 2l4 3.5L9 2" fill="none" stroke="#fff"/></svg>info@harbourlanerentals.com.au</div>
        <div class="contact-bar__line"><svg class="icon" viewBox="0 0 10 10"><circle cx="5" cy="5" r="4" fill="none" stroke="#fff"/><path d="M1 5h8M5 1v8" stroke="#fff" stroke-width=".7"/></svg>www.harbourlanerentals.com.au</div>
      </div>
    </div>
    <div class="contact-bar__divider"></div>
    <div class="contact-bar__social"><span class="social-square"></span><span class="social-square"></span></div>
  </footer>
</article>

<article class="page page--management">
  <div class="brand"><span class="brand__mark"></span><span class="brand__name">HARBOUR LANE RENTALS</span></div>
  <div class="hero" role="img" aria-label="Blue-toned photo of modern terraced townhouses with gardens along a street">
    <h1 class="hero__title">Lease and<br>Management Package</h1>
  </div>

  <section class="includes">
    <h2 class="section-heading"><svg class="chevron" viewBox="0 0 7 12"><path d="M1 1l5 5-5 5" fill="none" stroke="#1c65a3" stroke-width="2"/></svg>Includes:</h2>
    <ul class="feature-list">
      <li>Securing Tenant</li>
      <li>Reference/Database Checking</li>
      <li>Lease Preparation and Signing</li>
      <li>Direct Debit rent collection</li>
      <li>Zero arrears policy management</li>
      <li>Payment of Rates and levies</li>
      <li>Insurance management</li>
      <li>Coordination or all repairs and maintenance</li>
      <li>Regular rent reviews and renewals</li>
      <li>Detailed ingoing, ongoing and outgoing inspections with photos and videos viewable through your personal Landlord portal</li>
      <li>Bond management &nbsp;lodging and refunding</li>
      <li>Electronic monthly and EOFY statements</li>
      <li>Annual scheduled maintenance report</li>
      <li>Regulation/compliance management</li>
      <li>Tribunal Representation</li>
    </ul>
  </section>

  <section class="fees">
    <h2 class="section-heading">Management Rate</h2>
    <ul class="fee-list">
      <li class="fee-list__rate">Management Rate: 6% +GST of rental income</li>
      <li>Letting Fee: - 1 weeks rent+GST 6 or 12 month lease</li>
      <li>Advertising: $350 (Inc GST)</li>
      <li>Professional Photography: $199 (inc GST) 4 x Photos</li>
      <li>Statements: $5.00 Per month</li>
      <li>Lease Preperation: No Charge</li>
      <li>Renewal Fees: ½ Weeks Rent +GST</li>
    </ul>
  </section>
  <div class="side-photo" role="img" aria-label="Photo of a busy seaside promenade with cafe umbrellas beside the water"></div>

  <footer class="contact-bar">
    <div class="contact-bar__people">Tom Willard <span>✆ 0438 216 907</span><br>Marika Dunstan <span>✆ 0419 572 046</span></div>
    <div class="contact-bar__divider"></div>
    <div class="contact-bar__group contact-bar__address">
      <svg class="icon" viewBox="0 0 10 10"><path d="M5 1L1 5h1.3v4h2.2V6.5h1V9h2.2V5H9z" fill="#fff"/></svg>
      <div>Suite 7, 12-14 Carrow Parade,<br>Dee Why NSW 2099</div>
    </div>
    <div class="contact-bar__divider"></div>
    <div class="contact-bar__group contact-bar__web">
      <div>
        <div class="contact-bar__line"><svg class="icon" viewBox="0 0 10 10"><rect x="1" y="2" width="8" height="6" fill="none" stroke="#fff"/><path d="M1 2l4 3.5L9 2" fill="none" stroke="#fff"/></svg>info@harbourlanerentals.com.au</div>
        <div class="contact-bar__line"><svg class="icon" viewBox="0 0 10 10"><circle cx="5" cy="5" r="4" fill="none" stroke="#fff"/><path d="M1 5h8M5 1v8" stroke="#fff" stroke-width=".7"/></svg>www.harbourlanerentals.com.au</div>
      </div>
    </div>
    <div class="contact-bar__divider"></div>
    <div class="contact-bar__social"><span class="social-square"></span><span class="social-square"></span></div>
  </footer>
</article>

</body>
</html>
```